Design a Dynamic and User-Friendly Website for qGuestly: Revolutionize Visitor Management

Description of qGuestly:

qGuestly is an innovative online visitor management system designed to streamline the process of managing visitors in various organizational settings. Our system automates the check-in process, enhances security by keeping accurate visitor logs, and ensures compliance with local regulations through customizable features. With functionalities such as contactless sign-in, real-time notifications, visitor badge printing, and comprehensive reporting, qGuestly provides a modern solution to traditional visitor management challenges.

Target Audience:

Our primary target audience includes businesses and institutions across Africa, starting with Nigeria. This includes corporate offices, educational institutions, healthcare facilities, and government buildings that are looking for efficient, secure, and scalable visitor management solutions. Our system is particularly tailored to meet the needs of facility managers, security personnel, and front desk staff who prioritize ease of use, data security, and operational efficiency. Additionally, qGuestly aims to cater to IT managers looking for robust systems that can seamlessly integrate with existing organizational infrastructure.

Color Scheme:

While specific colors are not mandated, the chosen palette should convey trust and stability, growth and efficiency, and maintain a professional and clean appearance. The colors selected should harmonize to create a welcoming, secure, and efficient atmosphere.
Typography:

Use modern, sans-serif fonts for readability and a contemporary look. Primary text should be clear with high contrast against the background, and headings can be bold to create a hierarchical structure that is easy to navigate.
Imagery:

Photography: High-quality images that feature African professionals and contexts, illustrating diverse, professional scenarios relevant to our target industries (such as corporate offices, educational institutions, healthcare facilities). Photos should authentically represent the African demographic, showing interactions between people and technology, emphasizing the ease and security of the visitor management process.
Illustrations: Custom illustrations that should culturally resonate with African settings and characters, vividly depicting functionalities of qGuestly such as scanning a QR code, receiving a visitor badge, or receiving alerts on a smartphone or desktop. These illustrations should adopt a style that complements the overall design aesthetic of the site.
Layout and Design Elements:

A clean, minimalistic layout that focuses on usability with easy navigation paths for all user types.
Use cards or tiles for different sections such as features, testimonials, or case studies, which can help organize information cleanly and attractively.
Consider interactive elements like hover effects, animated transitions for loading elements, and subtle animations in illustrations to make the user experience dynamic and engaging.
Overall Theme:

The theme should be professional and welcoming, reflecting a high-tech solution that is approachable for users with varying levels of tech expertise. The design should instill confidence in the security and efficiency of the system, while also being culturally appropriate and user-friendly to encourage interaction and exploration of the site’s content.
This style and theme guide emphasizes flexibility in color usage while maintaining clear directives on the emotional and functional responses the design should invoke, ensuring it aligns with the values and needs of qGuestly's target audience.

What websites can designers draw inspiration from?
List websites you like and describe what you like about them.

https://entrypadhub.example/en-usremove
same industry so you can see their approaches to marketing to similar customers - granted their target is not specific to african market Very clean design and straight to the point. Their feature set is closest to our feature set.
http://www.gatelumo.exampleremove
clean design and straight to the point
http://lobbirant.exampleremove

Home Page
-------------------
Main Goal: Encourage visitors to start their 15-day free trial, effectively converting them into leads or potential customers.

Content Layout:
Hero Section: Engaging hero image or video that shows the qGuestly system in action, with clear, prominent call-to-action (CTA) buttons for "Start your 15 day free trial" and secondary CTA for "Buy now"

Product Overview: Quick introduction to what qGuestly is and its key benefits, such as enhanced security, easy integration, and improved operational efficiency.

Features Highlight: Brief visuals or icons depicting major features like contactless sign-in, real-time alerts, and comprehensive reporting.

How It Works: A concise step-by-step guide or graphic explaining how to get started with qGuestly.

CTA Section: A more detailed call to action for starting the free trial,
if they want a more hands on guide allow them to schedule a demo and if they are ready click purchase to buy now.
Footer: Navigation links to other site sections, social media links, and legal information.

-------------------
Pricing Page
-------------------
Main Goal: Clearly convey the pricing structure in a way that users can easily understand and compare options based on their location and specific needs.

Content Layout:

Pricing Introduction: Explain the subscription model, highlighting the flexibility and scalability of the service (i.e., per location and additional tablets).

Country-Specific Pricing Tabs: Tabs or a dropdown menu allowing users to choose their country (Nigeria, Ghana, South Africa, Kenya) to view localized pricing in the respective currencies (NGN, GHS, ZAR, KES).
Subscription Per Location: Detailed pricing for managing a single location, with benefits listed beside the price

Tablets and Data Plans: A clear breakdown of the cost per tablet and the associated wireless data plans, including bulk discount options if applicable.
Interactive Pricing Calculator: A tool that allows users to calculate their monthly cost based on the number of locations and tablets they plan to use.

Add ons - for hardware, etc

FAQs: A section dedicated to frequently asked questions specifically about pricing, billing cycles, and cancellation policies.

CTA: Strong call to action for starting a free trial, with an emphasis on the ease of signing up and the no-commitment nature of the trial.

Footer: Standard navigational links, contact information, and social media buttons.

-------------------
Feature Page Template
-------------------
Main Goal: To detail individual features of qGuestly, demonstrating the functionality and benefits to help prospective clients understand the value provided.

Content Layout:
Feature Introduction: Large title with a succinct description of the feature.

In-depth Details: Bullet points or short paragraphs explaining the feature, supported by relevant images or icons.

Use Case Scenario: Real-world application or a mini-case study showing the feature in action.

Benefit Summary: A list or graphic illustrating the benefits of the feature.

CTA: Prompt to try this feature via signup or schedule a demo speak with a sales representative.

Footer: Standard links and social media connections.

-------------------
Blog Page
-------------------
Main Goal: To engage current and prospective clients with useful content, position qGuestly as a thought leader in the visitor management space, and improve SEO rankings.

Content Layout:
Featured Article: Highlight a recent or popular post prominently at the top.

Article List: Thumbnails and summaries of additional articles with clear categorization (e.g., Tips, Case Studies, Industry News).

Search and Filter Tools: Allow users to filter blog posts by topic, date, etc.

Newsletter Signup: Encourage visitors to subscribe to updates.
Social Share Buttons: Enable easy sharing of articles.
Footer: Include a comprehensive footer with navigational links and contact info.

Generic Content Page (e.g., Contact Us, About Us)
------------------------------
Main Goal: To provide essential information about the qGuestly company or to facilitate contact with the company.

Content Layout:
Page Title and Introduction: Clear heading with a brief paragraph summarizing the page’s purpose.

Main Content Area: Detailed content appropriate to the page (e.g., company history, team bios for About Us; contact form, map, and helpline numbers for Contact Us).

Sidebar/Additional Elements: For Contact Us, include operational hours or a quick FAQ. For About Us, list awards or recognitions.

CTA: Depending on the page, direct users to other parts of the site (e.g., careers page link on About Us, newsletter sign-up on Contact Us).
Footer: Standard footer with expanded company details if on the Contact Us page.

Coding

```html
<!DOCTYPE html>
<html lang="en">
<head>
<meta charset="utf-8">
<title>qGuestly Feature</title>
<link href="https://fonts.googleapis.com/css2?family=Poppins:wght@400;500;600;700;800&display=swap" rel="stylesheet">
<style>
:root{
  --blue:#2b7fd4;
  --blue-light:#d6e7f8;
  --ink:#2e2e2e;
  --text:#555;
  --dark:#303030;
  --band:#ececec;
  --white:#fff;
}
*{box-sizing:border-box;margin:0;padding:0}
html,body{width:1200px;height:3533px;overflow:hidden}
body{font-family:'Poppins',sans-serif;color:var(--ink);background:var(--white);position:relative}
.abs{position:absolute}
.brand{font-weight:500;color:var(--blue);display:flex;align-items:center;gap:10px}
.brand .dot{width:34px;height:34px;border-radius:50%;border:4px solid var(--blue)}

/* nav */
.site-nav{top:30px;left:88px;width:1024px;height:44px;display:flex;align-items:center}
.site-nav .brand{font-size:36px}
.nav-links{display:flex;gap:30px;margin-left:95px;font-size:12px;font-weight:500;text-transform:uppercase;letter-spacing:.2px;align-items:center}
.nav-links .active{color:var(--blue)}
.btn{display:inline-flex;align-items:center;justify-content:center;font-weight:700;font-size:11.5px;text-transform:uppercase;border-radius:3px}
.btn-primary{background:var(--blue);color:var(--white)}
.btn-outline{border:2px solid currentColor}
.nav-cta{margin-left:35px;width:134px;height:37px}
.nav-login{margin-left:22px;font-size:12px;font-weight:700}

.page-title{top:140px;width:1200px;text-align:center;font-size:46px;font-weight:700}
.page-title span{color:var(--blue)}

.photo{border-radius:50%}
.hero-photo{left:206px;top:248px;width:354px;height:354px;background:radial-gradient(circle at 55% 40%,#8b7566,#3b3a3c 70%);box-shadow:0 12px 30px rgba(0,0,0,.15)}
.intro{left:609px;top:328px;width:410px;font-size:13.5px;line-height:19.5px;color:var(--text)}
.intro p+p{margin-top:13px}

.features{top:673px;left:88px;display:flex;gap:19px}
.feature-card{width:242px;height:343px;background:var(--white);border-radius:10px;box-shadow:0 8px 30px rgba(0,0,0,.08);text-align:center;padding:46px 20px 0}
.feature-card svg{width:76px;height:76px;stroke:var(--ink);fill:none;stroke-width:2}
.feature-card h3{font-size:17.5px;font-weight:600;line-height:22px;margin:22px 0 16px}
.feature-card p{font-size:12.5px;line-height:17.5px;color:var(--text)}

.case-band{top:1104px;left:0;width:1200px;height:690px}
.case-title{top:1172px;width:1200px;text-align:center;color:var(--white);font-size:31px;font-weight:700}
.case-text{left:185px;top:1285px;width:340px;color:var(--white)}
.case-text h2{font-size:36px;font-weight:700}
.case-text p{font-size:13.5px;line-height:19.5px;margin-top:10px}
.case-text .btn{margin-top:22px;width:107px;height:40px;color:var(--white)}
.side-word{left:1110px;top:1490px;transform:translate(-50%,-50%) rotate(-90deg);font-size:138px;font-weight:700;color:rgba(255,255,255,.14);white-space:nowrap}
.tablet{left:609px;top:1268px;width:413px;height:316px;background:#1d1d1f;border-radius:14px;padding:11px}
.tablet .screen{width:100%;height:100%;border-radius:6px;background:linear-gradient(180deg,#fafafa,#eef0f3)}
.phone{left:548px;top:1430px;width:131px;height:266px;background:#1d1d1f;border-radius:20px;padding:7px}
.phone .screen{width:100%;height:100%;border-radius:14px;background:var(--white);display:flex;align-items:center;justify-content:center}
.phone .brand{font-size:17px;gap:5px}
.phone .brand .dot{width:14px;height:14px;border-width:2px}

.benefits-title{top:1782px;width:1200px;text-align:center;font-size:31px;font-weight:600}
.timeline{left:599px;top:1865px;height:522px;border-left:2px dashed #cfd8e3}
.tl-dot{left:596px;width:9px;height:9px;border-radius:50%;background:var(--blue)}
.benefit h3{font-size:17.5px;font-weight:600}
.benefit p{font-size:12.5px;line-height:17.5px;color:var(--text);margin-top:10px}
.benefit.left{right:665px;width:340px;text-align:right}
.benefit.right{left:661px;width:350px}
.b-icon{width:84px;height:84px;stroke:var(--ink);fill:none;stroke-width:2}

.cta-photo{left:167px;top:2455px;width:461px;height:461px;background:radial-gradient(circle at 45% 45%,#6d7f96,#2f3540 75%)}
.cta-text{left:684px;top:2538px;width:350px}
.cta-text h2{font-size:36px;line-height:44px;font-weight:700}
.cta-text h2 span{color:var(--blue)}
.cta-text p{font-size:13.5px;line-height:19.5px;color:var(--text);margin-top:20px}
.cta-buttons{display:flex;gap:10px;margin-top:24px}
.cta-buttons .btn{height:41px}

.footer-shape{top:2820px;left:0;width:1200px;height:713px}
.footer-brand{top:3062px;width:1200px;justify-content:center;font-size:58px;color:var(--white)}
.footer-brand .dot{width:56px;height:56px;border-width:6px;border-color:var(--blue)}
.f-col{top:3190px;color:var(--white)}
.f-col h4{font-size:17.5px;font-weight:600;margin-bottom:20px}
.f-col ul{list-style:none;font-size:12.5px}
.f-col li{height:31.5px}
.f-col li::before{content:"›";color:#999;margin-right:7px}
.contact-item{display:flex;gap:10px;font-size:12.5px;line-height:17px;margin-bottom:14px}
.contact-item svg{width:14px;height:14px;flex:none;margin-top:2px;fill:var(--blue)}
.newsletter p{font-size:12.5px;line-height:17.5px;width:230px}
.nl-input{margin-top:14px;width:254px;height:44px;background:var(--white);border-radius:3px;display:flex;align-items:center;padding:0 14px;color:#555;font-size:12.5px;gap:8px}
.nl-input svg{width:16px;height:16px}
.socials{display:flex;gap:8px;margin-top:22px}
.socials span{width:31px;height:31px;border-radius:50%;background:#4a4a4a}
.foot-rule{top:3479px;left:88px;width:1024px;border-top:1px solid #4c4c4c}
.copyright{top:3497px;width:1200px;text-align:center;color:var(--white);font-size:12.5px}
.to-top{left:1129px;top:3459px;width:42px;height:42px;border-radius:50%;background:var(--blue);display:flex;align-items:center;justify-content:center}
</style>
</head>
<body>

<header class="abs site-nav">
  <div class="brand"><span class="dot"></span>qGuestly</div>
  <nav class="nav-links">
    <svg width="15" height="13" viewBox="0 0 16 14"><path d="M8 0 0 7h2v7h4V9h4v5h4V7h2z" fill="#2e2e2e"/></svg>
    <span>About us</span><span>Pricing</span><span>FAQs</span><span class="active">Featured</span><span>Blog</span><span>Contact us</span>
  </nav>
  <span class="btn btn-primary nav-cta">Start free trial</span>
  <span class="nav-login">LOGIN</span>
</header>

<h1 class="abs page-title"><span>qGuestly</span> Feature</h1>

<div class="abs photo hero-photo" role="img" aria-label="Photo of a professional woman holding a cup in a modern office lounge"></div>
<div class="abs intro">
  <p>At qGuestly, our story is one of innovation, perseverance, and dedication. From our humble beginnings to our current position as a market leader, we have remained committed to delivering cutting-edge solutions that meet the evolving needs of our clients. Our journey is defined by milestones such as [Highlight notable achievements or milestones].</p>
  <p>Revolutionize your visitor management with our innovative contactless sign-in feature, designed to prioritize safety and efficiency in your premises.</p>
</div>

<section class="abs features">
  <article class="feature-card">
    <svg viewBox="0 0 76 76"><path d="M4 18V4h14M58 4h14v14M72 58v14H58M18 72H4V58"/><rect x="26" y="14" width="24" height="48" rx="4"/><path d="M34 54h8"/></svg>
    <h3>QR Code<br>Technology</h3>
    <p>Utilize QR codes for touchless sign-in, allowing visitors to scan their unique code upon arrival, minimizing physical contact with shared surfaces.</p>
  </article>
  <article class="feature-card">
    <svg viewBox="0 0 76 76"><rect x="4" y="6" width="68" height="64" rx="3"/><path d="M4 16h68M12 28h30M12 38h24M12 48h20M12 60h36M48 54 66 24l4 3-18 30-5 2z"/></svg>
    <h3>Customizable<br>Sign-in Forms</h3>
    <p>Tailor sign-in forms to gather specific visitor information remotely, reducing wait times and enhancing data accuracy.</p>
  </article>
  <article class="feature-card">
    <svg viewBox="0 0 76 76"><circle cx="38" cy="38" r="16"/><rect x="32" y="37" width="12" height="9"/><path d="M34 37v-4a4 4 0 0 1 8 0v4M38 4v18M38 54v18M4 38h18M54 38h18M14 14l12 12M62 14 50 26M14 62l12-12M62 62 50 50"/><circle cx="38" cy="4" r="2"/><circle cx="4" cy="38" r="2"/><circle cx="72" cy="38" r="2"/><circle cx="38" cy="72" r="2"/></svg>
    <h3>Integration with<br>Access Control</h3>
    <p>Seamlessly integrate with your existing access control systems to automate the check-in process, granting authorized entry upon completion of sign-in.</p>
  </article>
  <article class="feature-card">
    <svg viewBox="0 0 76 76"><rect x="30" y="22" width="30" height="44" rx="2"/><path d="M24 30v42h30M37 36h16M37 44h16M37 52h12M8 30h16M8 46h16"/><circle cx="6" cy="30" r="3"/><circle cx="6" cy="46" r="3"/><circle cx="60" cy="18" r="10"/><circle cx="60" cy="18" r="4"/></svg>
    <h3>Real-time Data<br>Capture</h3>
    <p>Capture visitor data in real-time, enabling accurate tracking of visitor traffic for compliance, security, and operational purposes.</p>
  </article>
</section>

<svg class="abs case-band" viewBox="0 0 1200 690" preserveAspectRatio="none">
  <rect width="1200" height="690" fill="#2b7fd4"/>
  <polygon points="0,411 1200,686 1200,690 0,690" fill="#d6e7f8"/>
  <polygon points="0,456 1200,690 0,690" fill="#fff"/>
</svg>
<div class="abs side-word">qGuestly</div>
<h2 class="abs case-title">Case Studies</h2>
<div class="abs case-text">
  <h2>Setup</h2>
  <p>Aenean sollicitudin, lorem quis bibendum auctor, nisi elit consequat ipsum, nec sagittis sem nibh id elit. Duis sed odio sit amet nibh vulputate cursus sit amet mauris. Morbi accumsan ipsum velit. Nam nec tellus a odio tincidunt auctor...</p>
  <span class="btn btn-outline">Read more</span>
</div>
<div class="abs tablet"><div class="screen" role="img" aria-label="Screenshot of the qGuestly site settings dashboard"></div></div>
<div class="abs phone"><div class="screen"><div class="brand"><span class="dot"></span>qGuestly</div></div></div>

<h2 class="abs benefits-title">Our Benefits</h2>
<div class="abs timeline"></div>
<span class="abs tl-dot" style="top:1916px"></span>
<span class="abs tl-dot" style="top:2053px"></span>
<span class="abs tl-dot" style="top:2190px"></span>
<span class="abs tl-dot" style="top:2327px"></span>

<svg class="abs b-icon" style="left:451px;top:1880px" viewBox="0 0 84 84"><path d="M42 6 22 14v16c0 14 9 22 20 26 11-4 20-12 20-26V14z"/><path d="m33 30 7 7 12-13M6 40l10 22 12 12h10v-14l-12-10M78 40 68 62 56 74H46v-14l12-10"/></svg>
<div class="abs benefit right" style="top:1872px"><h3>Enhanced Safety</h3><p>Minimize the risk of germ transmission through shared touch surfaces, promoting a safer environment for visitors and staff.</p></div>

<div class="abs benefit left" style="top:2008px"><h3>Streamlined Experience</h3><p>Reduce wait times and improve efficiency by enabling visitors to complete the sign-in process quickly and easily.</p></div>
<svg class="abs b-icon" style="left:661px;top:2012px;width:92px;height:92px" viewBox="0 0 92 92"><circle cx="46" cy="20" r="8"/><circle cx="46" cy="20" r="15" stroke-dasharray="6 4"/><circle cx="46" cy="70" r="8"/><circle cx="46" cy="70" r="15" stroke-dasharray="6 4"/><circle cx="10" cy="45" r="6"/><circle cx="82" cy="45" r="6"/><path d="M16 45h60M46 35v20"/></svg>

<svg class="abs b-icon" style="left:453px;top:2150px;width:84px;height:92px" viewBox="0 0 84 92"><rect x="4" y="10" width="58" height="76" rx="3"/><rect x="22" y="4" width="22" height="12" rx="2"/><path d="M14 30h8v8h-8zM14 48h8v8h-8zM14 66h8v8h-8zM30 34h22M30 52h22M30 70h14"/><circle cx="66" cy="72" r="14"/><path d="m59 72 5 5 9-10"/></svg>
<div class="abs benefit right" style="top:2145px"><h3>Improved Compliance</h3><p>Maintain accurate records of visitor traffic, ensuring compliance with regulatory requirements and security protocols.</p></div>

<div class="abs benefit left" style="top:2282px"><h3>Integration</h3><p>Capabilities: Seamlessly integrate with your existing access control systems for a cohesive visitor management solution.</p></div>
<svg class="abs b-icon" style="left:661px;top:2280px;width:80px;height:102px" viewBox="0 0 80 102"><circle cx="40" cy="70" r="12"/><circle cx="40" cy="70" r="24" stroke-dasharray="8 5"/><path d="M40 4v42M28 10v28l6 10M52 10v28l-6 10M16 20v18l14 14M64 20v18L50 52"/><circle cx="40" cy="4" r="3"/><circle cx="28" cy="8" r="3"/><circle cx="52" cy="8" r="3"/><circle cx="16" cy="18" r="3"/><circle cx="64" cy="18" r="3"/></svg>

<div class="abs photo cta-photo" role="img" aria-label="Photo of a visitor signing in at a clinic reception desk with a staff member holding a clipboard"></div>
<div class="abs cta-text">
  <h2>Ready to Get<br><span>Started?</span></h2>
  <p>Experience the benefits of qGuestly today with our 15-day free trial. Take the first step towards efficient, secure, and compliant visitor management for your organization.</p>
  <div class="cta-buttons">
    <span class="btn btn-primary" style="width:213px">Start your 15 day free trial</span>
    <span class="btn btn-outline" style="width:106px;color:var(--ink)">Buy now</span>
  </div>
</div>

<svg class="abs footer-shape" viewBox="0 0 1200 713" preserveAspectRatio="none">
  <polygon points="0,270 1200,12 1200,713 0,713" fill="#ececec"/>
  <polygon points="0,282 1200,53 1200,713 0,713" fill="#303030"/>
</svg>
<div class="abs brand footer-brand"><span class="dot"></span>qGuestly</div>

<div class="abs f-col" style="left:170px"><h4>Quick links</h4>
  <ul><li>About Us</li><li>Pricing</li><li>FAQs</li><li>Featured</li><li>Blog</li><li>Contact Us</li></ul></div>
<div class="abs f-col" style="left:384px"><h4>Information</h4>
  <ul><li>Terms &amp; Condition</li><li>Privacy Policy</li><li>Site Map</li><li>Disclaimer</li><li>Reviews</li><li>Legal Information</li></ul></div>
<div class="abs f-col" style="left:585px"><h4>Contact info</h4>
  <div class="contact-item"><svg viewBox="0 0 16 16"><path d="M1 3h14v10H1zM1 3l7 6 7-6" /></svg><span>Email:<br>info@qguestly.example</span></div>
  <div class="contact-item"><svg viewBox="0 0 16 16"><path d="M3 1h3l1 4-2 1c1 2 3 4 5 5l1-2 4 1v3c0 1-1 2-2 2C7 15 1 9 1 3c0-1 1-2 2-2z"/></svg><span>Phone:<br>(555) 010-2468</span></div>
  <div class="contact-item"><svg viewBox="0 0 16 16"><circle cx="8" cy="8" r="7"/></svg><span>Web:<br>www.qguestly.example</span></div>
</div>
<div class="abs f-col newsletter" style="left:802px"><h4>Newsletter</h4>
  <p>Subscribe to our email address to get the latest news.</p>
  <div class="nl-input"><svg viewBox="0 0 16 16" fill="#999"><path d="M1 3h14v10H1z"/></svg><span style="flex:1">Enter Your Email...</span><svg viewBox="0 0 16 16" fill="#2b7fd4"><path d="M15 1 1 7l5 2 2 6z"/></svg></div>
  <div class="socials"><span></span><span></span><span></span><span></span></div>
</div>

<div class="abs foot-rule"></div>
<p class="abs copyright">© Copyright 2024 All Rights Reserved</p>
<div class="abs to-top"><svg width="14" height="16" viewBox="0 0 14 16"><path d="M7 15V2M2 7l5-5 5 5" stroke="#fff" stroke-width="2" fill="none"/></svg></div>

</body>
</html>
```